Flyer for the Lumen 2025 Conference

I am looking to produce a flyer for our upcoming conference, Lumen 2025. This is an annual conference that we plan to publicize on social media. The ideal designer will create a flyer that is eye-catching and effectively communicates the key information. Please see attached our logo, speaker photo, and flyer content.

Target Market(s)

All demographics

Industry/Entity Type

Christian

Font styles to use
Sans Serif

Requirements
Should not have
• Cross, church

```html
<!DOCTYPE html>
<html lang="en">
<head>
<meta charset="utf-8">
<title>Lumen 2025 Conference Flyer</title>
<link href="https://fonts.googleapis.com/css2?family=Red+Hat+Display:wght@400;500;600;700;900&display=swap" rel="stylesheet">
<style>
  :root{
    --bg:#e6e6e8;
    --navy:#2a2466;
    --indigo:#3a2f94;
    --ray:#4a6cff;
    --ray-bright:#9fd0ff;
    --panel:rgba(40,32,100,.82);
    --orange:#f0a12e;
    --white:#ffffff;
    --soft:#e4e2ff;
    --suit:#1e7fd0;
    --pin:#e5353f;
    --app:#3d7cf0;
  }
  *{margin:0;padding:0;box-sizing:border-box}
  html,body{width:1200px;height:800px;overflow:hidden;background:var(--bg);
    font-family:"Red Hat Display",Arial,sans-serif;color:var(--white)}
  .flyer{position:absolute;left:330px;top:17px;width:540px;height:766px;overflow:hidden;
    background:
      radial-gradient(ellipse 60% 45% at 52% 0%, rgba(159,208,255,.9), rgba(74,108,255,.55) 35%, transparent 70%),
      linear-gradient(180deg, rgba(42,36,102,0) 0%, rgba(42,36,102,0) 30%, var(--navy) 62%),
      repeating-linear-gradient(90deg, rgba(120,170,255,0) 0 18px, rgba(120,170,255,.12) 18px 26px, rgba(120,170,255,0) 26px 44px),
      linear-gradient(180deg, var(--indigo) 0%, var(--navy) 55%, #2b2468 100%);
  }
  .flyer::after{content:"";position:absolute;inset:0;
    background:radial-gradient(ellipse 70% 18% at 50% 72%, rgba(70,90,210,.28), transparent 80%);
    pointer-events:none}
  .speaker-photo{position:absolute;left:39px;top:169px;width:227px;height:275px;border-radius:110px 110px 0 0;
    background:linear-gradient(180deg, #3c3a78 0%, var(--suit) 45%, #155fa8 100%);z-index:1}
  .title-block{position:absolute;left:230px;top:132px;width:256px;text-align:center;z-index:2}
  .title{font-weight:900;font-size:58px;line-height:1;letter-spacing:.5px}
  .year{font-weight:500;font-size:60px;line-height:1;margin-top:2px}
  .subtitle{font-weight:500;font-size:20px;margin-top:6px;white-space:nowrap}
  .info{position:absolute;left:230px;width:256px;text-align:center;font-size:16px;line-height:1.25;z-index:2}
  .info .label{font-weight:400}
  .info .value{font-weight:600}
  .topic{top:310px}
  .speaker{top:369px}
  .dates{position:absolute;left:58px;top:444px;width:420px;height:92px;border-radius:10px;
    background:var(--panel);display:flex;z-index:2}
  .dates-tab{width:33px;background:var(--orange);border-radius:10px 0 0 10px;display:flex;
    align-items:center;justify-content:center}
  .dates-tab span{transform:rotate(-90deg);font-weight:900;font-size:19px;letter-spacing:.5px}
  .day{flex:1;padding:17px 0 0 14px;font-size:12px;line-height:1.1}
  .day .num{font-weight:900;font-size:30px;line-height:1}
  .day sup{font-size:16px;font-weight:900;vertical-align:top;position:relative;top:-2px}
  .venue{position:absolute;left:58px;top:555px;display:flex;align-items:center;gap:16px;z-index:2;font-size:12.5px;line-height:1.35;color:var(--soft)}
  .icon-box{width:32px;height:32px;background:var(--white);border-radius:6px;display:flex;align-items:center;justify-content:center}
  .brand{position:absolute;left:58px;top:645px;width:160px;height:40px;display:flex;align-items:center;gap:8px;z-index:2;white-space:nowrap}
  .brand-dot{width:10px;height:10px;border-radius:50%;background:var(--orange);flex:none}
  .brand-name{font-weight:500;font-size:30px;letter-spacing:.5px;line-height:1}
  .app-pill{position:absolute;left:232px;top:646px;width:233px;height:40px;border-radius:20px;
    background:rgba(40,32,100,.7);display:flex;align-items:center;gap:16px;z-index:2;font-size:12.5px;line-height:1.1;white-space:nowrap}
  .app-icon{width:38px;height:38px;border-radius:10px;background:var(--app);display:flex;align-items:center;justify-content:center;flex:none}
  .app-pill b{font-weight:700}
  .contacts{position:absolute;left:58px;top:703px;display:flex;gap:20px;z-index:2;font-size:13px;align-items:center;white-space:nowrap}
  .contact{display:flex;align-items:center;gap:9px}
  .circle{width:22px;height:22px;border-radius:50%;background:var(--white);display:flex;align-items:center;justify-content:center}
</style>
</head>
<body>
<main class="flyer">
  <div class="speaker-photo" role="img" aria-label="Photo of the conference speaker in a blue suit"></div>

  <header class="title-block">
    <h1 class="title">LUMEN</h1>
    <div class="year">2025</div>
    <div class="subtitle">A Prophetic Conference</div>
  </header>

  <section class="info topic">
    <div class="label">Topic:</div>
    <div class="value">The Voice Of The Lord</div>
  </section>
  <section class="info speaker">
    <div class="label">Speaker:</div>
    <div class="value">Prophet Samuel Kerr</div>
  </section>

  <section class="dates">
    <div class="dates-tab"><span>DATES</span></div>
    <div class="day">Friday, December<div class="num">26<sup>th</sup></div>6:30 PM - 9:00 PM</div>
    <div class="day">Saturday, December<div class="num">27<sup>th</sup></div>5:30 PM - 8:00 PM</div>
    <div class="day">Sunday, December<div class="num">29<sup>th</sup></div>4:30 PM - 7:00 PM</div>
  </section>

  <section class="venue">
    <div class="icon-box">
      <svg width="16" height="20" viewBox="0 0 16 20"><path d="M8 0a8 8 0 0 0-8 8c0 5.5 8 12 8 12s8-6.5 8-12a8 8 0 0 0-8-8z" fill="var(--pin)"/><circle cx="8" cy="8" r="3.2" fill="#fff"/></svg>
    </div>
    <div>The Harbor Arts Center 128 Linden Avenue<br>Brookfield, Maine 04011</div>
  </section>

  <div class="brand"><span class="brand-dot"></span><span class="brand-name">VESTRA</span></div>

  <div class="app-pill">
    <div class="app-icon">
      <svg width="18" height="18" viewBox="0 0 18 18" fill="none" stroke="#fff" stroke-width="1.8" stroke-linecap="round"><path d="M9 2v9M5 7.5 9 11.5 13 7.5M3 12.5v3h12v-3"/></svg>
    </div>
    <div>Download the <b>VESTRA App</b><br>to stay updated on the event</div>
  </div>

  <footer class="contacts">
    <div class="contact"><span class="circle"><svg width="12" height="12" viewBox="0 0 24 24"><path d="M6.6 10.8a15 15 0 0 0 6.6 6.6l2.2-2.2a1 1 0 0 1 1-.25 11.4 11.4 0 0 0 3.6.6 1 1 0 0 1 1 1V20a1 1 0 0 1-1 1A17 17 0 0 1 3 4a1 1 0 0 1 1-1h3.5a1 1 0 0 1 1 1c0 1.25.2 2.45.6 3.6a1 1 0 0 1-.25 1z" fill="var(--navy)"/></svg></span>555 014 2290</div>
    <div class="contact"><span class="circle"><svg width="12" height="10" viewBox="0 0 12 10" fill="none" stroke="var(--navy)" stroke-width="1.3"><rect x=".7" y=".7" width="10.6" height="8.6" rx="1"/><path d="M1 1l5 4.5L11 1"/></svg></span>hello@vestra.org</div>
    <div class="contact"><span class="circle"><svg width="13" height="13" viewBox="0 0 14 14" fill="none" stroke="var(--navy)" stroke-width="1.1"><circle cx="7" cy="7" r="6"/><ellipse cx="7" cy="7" rx="2.6" ry="6"/><path d="M1 7h12M2 4h10M2 10h10"/></svg></span>www.vestra.org</div>
  </footer>
</main>
</body>
</html>
```